Website design for commercial and residential security company

we're looking to see some new designs for an established company with no website.

homepage and one inner page

here is a link to the homepage content, sitemap, logo and more.
https://files.trovelink-share.net/folders/7QmzKpw3RtvxnLa9eHs2YcdJfuoPb?view=open

call to action should be Request A Quote

if you have any questions please send them to us asap

thank you

Number of Pages Required

1 page

Font styles to use
Sans Serif

```html
<!DOCTYPE html>
<html lang="en">
<head>
<meta charset="utf-8">
<title>Ardenmoor Business Solutions</title>
<link href="https://fonts.googleapis.com/css2?family=Oswald:wght@300;400;500;600&family=Roboto:wght@400;500;700&display=swap" rel="stylesheet">
<style>
:root{
  --gold:#c9a632;
  --gold-light:#d6b945;
  --ink:#141414;
  --dark:#0e0e0e;
  --strip:#1b1b1b;
  --text:#ffffff;
  --muted:#b8b8b8;
  --body:#555555;
  --paper:#ffffff;
  --mist:#f1f0ec;
  --line:#3d3d3d;
}
*{box-sizing:border-box;margin:0;padding:0}
html,body{width:1200px;height:3973px;overflow:hidden;background:var(--paper)}
body{font-family:"Roboto",sans-serif;color:var(--text);position:relative}
.page{position:relative;width:1200px;height:3973px;overflow:hidden}
section,header,footer{position:absolute;left:0;width:1200px;overflow:hidden}
.abs{position:absolute}
h1,h2,h3,h4{line-height:1.2;white-space:nowrap}
.btn{position:absolute;display:flex;align-items:center;justify-content:center;gap:12px;background:var(--gold);color:#fff;font-size:14px;font-weight:500}
.btn.outline{background:transparent;border:2px solid #fff}
.btn .label{font-family:"Oswald",sans-serif;font-weight:500;letter-spacing:.3px;font-size:15px}

/* hero */
.hero{top:0;height:623px;background:linear-gradient(90deg,#1a1a1a 0%,#222 55%,#2b2b2b 100%)}
.hero-photo{left:740px;top:0;width:460px;height:623px;background:radial-gradient(circle at 60% 40%,#3a3a3a,#111 55%,#d8d8d8 100%)}
.topbar{left:0;top:0;width:1200px;height:97px;border-bottom:1px solid #333}
.brand{position:absolute;display:flex;align-items:center;gap:8px;font-family:"Oswald",sans-serif;font-weight:500;color:#fff;font-size:24px;letter-spacing:.5px;line-height:1.2}
.brand .mark{width:14px;height:14px;border-radius:50%;background:var(--gold)}
.call{left:617px;top:30px;display:flex;gap:20px;align-items:center}
.call small{display:block;color:var(--gold);font-size:13px}
.call strong{display:block;font-size:16px;font-weight:500;margin-top:4px}
.nav{left:172px;top:122px;display:flex;gap:40px;font-size:13px;font-weight:500}
.nav .active{color:var(--gold)}
.hero h2{left:157px;top:232px;font-family:"Oswald",sans-serif;font-weight:300;font-size:34px;line-height:40px;color:#fff}
.hero h1{left:157px;top:280px;font-family:"Oswald",sans-serif;font-weight:600;font-size:60px;line-height:62px;color:var(--gold);letter-spacing:.5px}
.hero p{left:157px;top:354px;width:560px;font-size:14px;line-height:26px;color:#eee}
.dots{left:157px;top:532px;display:flex;gap:20px;align-items:center}
.dots i{display:block;width:7px;height:7px;border-radius:50%;background:var(--gold)}
.dots i.on{width:12px;height:12px;background:none;border:2px solid #aaa}

/* welcome */
.welcome{top:623px;height:498px;background:var(--paper);color:var(--body)}
.ph-a{left:301px;top:48px;width:345px;height:262px;background:linear-gradient(135deg,#eeeeee,#c9c9c9)}
.ph-b{left:72px;top:183px;width:346px;height:263px;background:linear-gradient(135deg,#d7dde4,#8a98a8)}
.dot-field{width:90px;height:70px;background:#f1f1f1}
.welcome .kicker{left:686px;top:62px;font-family:"Oswald",sans-serif;font-weight:300;font-size:24px;line-height:30px;color:#222}
.welcome h3{left:686px;top:96px;font-family:"Oswald",sans-serif;font-weight:500;font-size:26px;line-height:32px;color:var(--gold)}
.welcome .mission{left:686px;top:151px;font-size:12px;font-weight:500;color:var(--gold)}
.welcome .copy{left:686px;width:380px;font-size:12px;line-height:24px;color:#666}

/* tabs */
.tabs{top:1121px;height:93px;display:flex}
.tab{width:600px;height:93px;display:flex;align-items:center;justify-content:center;gap:22px;font-family:"Oswald",sans-serif;font-size:25px;font-weight:400;color:#fff;background:var(--gold)}
.tab+.tab{background:var(--gold-light);border-left:1px solid #b8962a}

/* services */
.services{top:1214px;height:424px;background:radial-gradient(circle at 50% 40%,#1d1d1d,#070707 70%)}
.svc{position:absolute;top:91px;width:156px;height:211px;border:1px solid var(--line);background:rgba(12,12,12,.85);text-align:center}
.svc svg{margin-top:38px}
.svc .name{margin-top:12px;font-size:12px;line-height:19px;color:#eee}
.svc .chev{margin-top:8px}
.svc .bar{position:absolute;left:60px;bottom:-1px;width:36px;height:3px;background:var(--gold)}
.tagline{left:0;top:362px;width:1200px;text-align:center;font-size:13px;color:#ddd}
.tagline span{color:var(--gold)}

/* feature bands */
.band{height:465px}
.res{top:1638px;background:linear-gradient(90deg,#0f1418 0%,#1b2126 40%,#5a4430 70%,#2c2a24 100%)}
.com{top:2103px;height:471px;background:linear-gradient(90deg,#8a6a2c 0%,#4d6fb0 35%,#334f8c 60%,#1f2f56 100%)}
.band h3{font-family:"Oswald",sans-serif;font-weight:500;font-size:25px;color:var(--gold)}
.band .lead{font-size:14px;line-height:24px;color:#fff}
.band .copy{font-size:12px;line-height:24px;color:#cfcfcf}

/* gallery */
.gallery{top:2574px;height:606px;background:var(--paper)}
.gallery h2{left:0;width:1200px;top:28px;text-align:center;font-family:"Oswald",sans-serif;font-weight:500;font-size:25px;color:#222}
.gallery h2 span{color:var(--gold)}
.tile{position:absolute}

/* quote */
.quote{top:3180px;height:453px;background:var(--mist)}
.quote-photo{left:0;top:0;width:570px;height:453px;background:linear-gradient(135deg,#d9d2c8,#a98f74 60%,#e8e4df)}
.quote h3{left:629px;font-family:"Oswald",sans-serif;font-weight:500;font-size:25px;line-height:30px}
.quote p{left:629px;top:142px;width:360px;font-size:12px;line-height:20px;color:#777}
.field{position:absolute;width:196px;height:49px;border:1px solid #d8d8d8;background:#fbfbfa;font-size:12px;color:#aaa;padding:16px 22px}

/* contact strip */
.contact{top:3633px;height:96px;background:var(--strip)}
.citem{position:absolute;top:38px;display:flex;align-items:center;gap:12px;font-size:12px;color:#fff;white-space:nowrap}
.citem b{font-weight:700}
.divider{position:absolute;top:0;width:1px;height:96px;background:#3a3a3a}
.divider::after{content:"";position:absolute;left:-3px;bottom:-3px;width:7px;height:7px;border-radius:50%;background:var(--gold)}

/* footer */
.footer{top:3729px;height:199px;background:#121212}
.footer h4{position:absolute;top:55px;font-size:11px;font-weight:700;color:var(--gold);letter-spacing:.3px}
.flinks{position:absolute;top:83px;font-size:12px;line-height:24px;color:#bbb}
.social{position:absolute;left:810px;top:86px;display:flex;gap:15px}
.social i{display:block;width:28px;height:28px;border-radius:50%;background:var(--gold)}
.copyright{top:3928px;height:45px;background:var(--gold);text-align:center;font-size:11px;line-height:45px;color:#fff}
.copyright b{font-weight:700}
</style>
</head>
<body>
<div class="page">

<header class="hero">
  <div class="abs hero-photo" role="img" aria-label="Close-up photograph of a black smart security camera mounted on a wall"></div>
  <div class="abs topbar"></div>
  <div class="brand" style="left:154px;top:34px"><span class="mark"></span>ARDENMOOR</div>
  <div class="abs call">
    <svg width="36" height="36" viewBox="0 0 36 36" fill="none" stroke="#c9a632" stroke-width="2"><rect x="6" y="3" width="18" height="30" rx="3"/><path d="M12 28h6M26 10a6 6 0 0 1 0 10M29 7a10 10 0 0 1 0 16"/></svg>
    <div><small>Make a Call</small><strong>(555) 014 - 2290</strong></div>
  </div>
  <div class="btn" style="left:843px;top:26px;width:201px;height:48px">
    <svg width="26" height="22" viewBox="0 0 26 22" fill="none" stroke="#fff" stroke-width="1.8"><path d="M3 3h20v13H10l-5 4v-4H3z"/><path d="M9 8v3M13 8v3M17 8v3"/></svg>
    <span style="font-size:13px;font-weight:700">REQUEST A QUOTE</span>
  </div>
  <nav class="abs nav"><span class="active">Home</span><span>About us</span><span>Solutions</span><span>Resources</span><span>Contact</span></nav>
  <h2 class="abs">PROTECT YOUR</h2>
  <h1 class="abs">BUSINESS &amp; HOME NOW</h1>
  <p class="abs">To provide our customers with comprehensive security, audio/video, and automation with top notch customer service. We Ensure Security with Smart Tools.</p>
  <div class="btn" style="left:157px;top:432px;width:196px;height:55px">
    <svg width="30" height="30" viewBox="0 0 30 30" fill="none" stroke="#fff" stroke-width="1.6"><rect x="5" y="4" width="14" height="23"/><rect x="19" y="12" width="7" height="15"/><path d="M8 8h3M13 8h3M8 13h3M13 13h3M8 18h3M13 18h3M10 27v-4h4v4"/></svg>
    <span class="label">COMMERCIAL</span>
  </div>
  <div class="btn outline" style="left:373px;top:432px;width:188px;height:55px">
    <svg width="30" height="30" viewBox="0 0 30 30" fill="none" stroke="#fff" stroke-width="1.6"><path d="M3 14L15 4l12 10M6 12v14h18V12"/><rect x="12" y="17" width="6" height="9"/></svg>
    <span class="label">RESIDENTIAL</span>
  </div>
  <div class="abs dots"><i></i><i class="on"></i><i></i></div>
</header>

<section class="welcome">
  <div class="abs dot-field" style="left:205px;top:100px"></div>
  <div class="abs dot-field" style="left:428px;top:320px;height:90px"></div>
  <div class="abs ph-a" role="img" aria-label="Photograph of a wall-mounted smart home control tablet"></div>
  <div class="abs ph-b" role="img" aria-label="Photograph of a man using a security keypad on the wall"></div>
  <div class="abs kicker">WELCOME TO</div>
  <h3 class="abs">ARDENMOOR BUSINESS SOLUTIONS</h3>
  <div class="abs mission">OUR MISSION</div>
  <p class="abs copy" style="top:177px">To provide our customers with comprehensive security, audio/video, and automation with top notch customer service. We Ensure Security with Smart Tools.</p>
  <p class="abs copy" style="top:268px">The graded security measures from Ardenmoor Business Solutions ensure the safety of both residential and commercial property. We provide a wide range of Residential and Commercial Security Solutions.</p>
  <div class="btn" style="left:688px;top:387px;width:132px;height:37px">Read More</div>
</section>

<section class="tabs">
  <div class="tab">
    <svg width="34" height="34" viewBox="0 0 30 30" fill="none" stroke="#fff" stroke-width="1.4"><rect x="5" y="4" width="14" height="23"/><rect x="19" y="12" width="7" height="15"/><path d="M8 8h3M13 8h3M8 13h3M13 13h3M8 18h3M13 18h3M10 27v-4h4v4"/></svg>
    <span>Commercial Security Solutions</span>
    <svg width="20" height="14" viewBox="0 0 20 14" fill="none" stroke="#fff" stroke-width="2.4"><path d="M3 3l7 7 7-7"/></svg>
  </div>
  <div class="tab">
    <svg width="36" height="34" viewBox="0 0 30 30" fill="none" stroke="#fff" stroke-width="1.4"><path d="M3 14L15 4l12 10M6 12v14h18V12"/><rect x="12" y="17" width="6" height="9"/></svg>
    <span>Residential Security Solutions</span>
    <svg width="14" height="20" viewBox="0 0 14 20" fill="none" stroke="#fff" stroke-width="2.4"><path d="M3 3l7 7-7 7"/></svg>
  </div>
</section>

<section class="services">
  <div class="svc" style="left:154px">
    <svg width="70" height="70" viewBox="0 0 70 70" fill="none" stroke="#c9a632" stroke-width="2"><rect x="10" y="10" width="34" height="16"/><path d="M44 14h12v8H44M20 26v16h-8M20 34h14v14M24 56h18v10H24z"/></svg>
    <div class="name">Audio<br>&amp; Video</div>
    <svg class="chev" width="12" height="8" viewBox="0 0 12 8" fill="none" stroke="#fff" stroke-width="1.6"><path d="M2 2l4 4 4-4"/></svg>
    <div class="bar"></div>
  </div>
  <div class="svc" style="left:337px">
    <svg width="70" height="70" viewBox="0 0 70 70" fill="none" stroke="#c9a632" stroke-width="2"><path d="M23 22a12 12 0 0 1 24 0v8H23z"/><rect x="22" y="34" width="26" height="18" rx="3"/><path d="M28 40h14M28 46h14M35 4v5M20 9l3 4M50 9l-3 4M14 36a18 18 0 0 0 0 16M56 36a18 18 0 0 1 0 16"/></svg>
    <div class="name">Burglar Alarms &amp;<br>Detectors</div>
    <svg class="chev" width="12" height="8" viewBox="0 0 12 8" fill="none" stroke="#fff" stroke-width="1.6"><path d="M2 2l4 4 4-4"/></svg>
    <div class="bar"></div>
  </div>
  <div class="svc" style="left:520px">
    <svg width="70" height="70" viewBox="0 0 70 70" fill="none" stroke="#c9a632" stroke-width="2"><rect x="10" y="12" width="46" height="16" rx="8"/><circle cx="22" cy="20" r="4"/><path d="M36 28v12h14v22h8V36M56 20h6"/></svg>
    <div class="name">CCTV<br>Camera</div>
    <svg class="chev" width="12" height="8" viewBox="0 0 12 8" fill="none" stroke="#fff" stroke-width="1.6"><path d="M2 2l4 4 4-4"/></svg>
    <div class="bar"></div>
  </div>
  <div class="svc" style="left:703px">
    <svg width="70" height="70" viewBox="0 0 70 70" fill="none" stroke="#c9a632" stroke-width="2"><path d="M24 50V34a11 11 0 0 1 22 0v16M18 50h34v8H18zM35 4v8M16 12l5 6M54 12l-5 6M8 30h7M55 30h7"/><circle cx="35" cy="38" r="3"/></svg>
    <div class="name">Monitoring<br>of Alarms</div>
    <svg class="chev" width="12" height="8" viewBox="0 0 12 8" fill="none" stroke="#fff" stroke-width="1.6"><path d="M2 2l4 4 4-4"/></svg>
    <div class="bar"></div>
  </div>
  <div class="svc" style="left:886px">
    <svg width="70" height="70" viewBox="0 0 70 70" fill="none" stroke="#c9a632" stroke-width="2"><path d="M14 20h42v14a21 21 0 0 1-42 0z"/><circle cx="35" cy="34" r="8"/><path d="M26 8h18v12H26zM56 14h6"/></svg>
    <div class="name">IP Cameras</div>
    <svg class="chev" width="12" height="8" viewBox="0 0 12 8" fill="none" stroke="#fff" stroke-width="1.6" style="margin-top:27px"><path d="M2 2l4 4 4-4"/></svg>
    <div class="bar"></div>
  </div>
  <div class="abs tagline">Providing Smart security for the smart generation. <span>Let's Get Started</span></div>
</section>

<section class="band res" role="img" aria-label="Photograph of a modern wooden house lit at dusk among trees">
  <h3 class="abs" style="left:157px;top:74px">Residential Security Solutions</h3>
  <p class="abs lead" style="left:157px;top:130px;width:380px">Consider a home surveillance device that would do more for you and your family than you ever imagined.</p>
  <p class="abs copy" style="left:157px;top:194px;width:370px">Ardenmoor Business Solutions is your trustable security provider. Also, as certified professionals carry out the installation, you have everything under control. Your home is being securely watched from various points, with cameras capable of tracking any intruder's path.</p>
  <div class="btn" style="left:162px;top:347px;width:125px;height:40px">Read More</div>
</section>

<section class="band com" role="img" aria-label="Photograph of a modern glass office building with autumn trees">
  <h3 class="abs" style="left:751px;top:96px">Commercial Solutions</h3>
  <p class="abs lead" style="left:751px;top:149px;width:370px">Protect assets and security of your business with Exceptional Commercial Security Installation</p>
  <p class="abs copy" style="left:751px;top:213px;width:350px">People's safety is our top priority. This includes ensuring that the security system built at your commercial property is configured accurately. Further, it will protect against intruders, burglaries, and holdups. We do this by:</p>
  <div class="btn" style="left:753px;top:333px;width:126px;height:40px">Read More</div>
</section>

<section class="gallery">
  <h2 class="abs">OUR <span>GALLERY</span></h2>
  <div class="tile" style="left:156px;top:94px;width:432px;height:199px;background:linear-gradient(135deg,#b9c3cf,#e6e9ed)" role="img" aria-label="Photograph of a technician drilling to mount a security camera"></div>
  <div class="tile" style="left:614px;top:94px;width:432px;height:199px;background:linear-gradient(135deg,#d7d3cc,#f3f1ee)" role="img" aria-label="Photograph of a dome camera and a phone showing the camera feed"></div>
  <div class="tile" style="left:156px;top:334px;width:279px;height:198px;background:linear-gradient(135deg,#c8ccb8,#e9eadf)" role="img" aria-label="Photograph of a video intercom panel on a wall"></div>
  <div class="tile" style="left:461px;top:334px;width:279px;height:198px;background:linear-gradient(135deg,#e4e4e4,#bdbdbd)" role="img" aria-label="Photograph of a hand holding a small round indoor camera"></div>
  <div class="tile" style="left:763px;top:334px;width:279px;height:198px;background:linear-gradient(135deg,#d9d6d1,#9aa0a6)" role="img" aria-label="Photograph of a woman and child using a wall-mounted security panel"></div>
</section>

<section class="quote">
  <div class="abs quote-photo" role="img" aria-label="Photograph of a father and son using a smart home touch panel"></div>
  <h3 class="abs" style="top:48px;color:#222">INTRODUCING THE MOST</h3>
  <h3 class="abs" style="top:85px;color:var(--gold)">EASIEST SECURITY SYSTEMS</h3>
  <p class="abs">Aorem ipsum dolor sit amet consectetur adipisicing anim elit dolore magna aliqua veniam quis nostrud.</p>
  <div class="field" style="left:626px;top:208px">Name</div>
  <div class="field" style="left:847px;top:208px">Email Address</div>
  <div class="field" style="left:626px;top:276px">Phone Number</div>
  <div class="field" style="left:847px;top:276px;padding-top:22px">Message</div>
  <div class="btn" style="left:629px;top:356px;width:193px;height:53px">
    <svg width="28" height="24" viewBox="0 0 26 22" fill="none" stroke="#fff" stroke-width="1.8"><path d="M3 3h20v13H10l-5 4v-4H3z"/><path d="M9 8v3M13 8v3M17 8v3"/></svg>
    <span style="font-size:13px;font-weight:700">REQUEST A QUOTE</span>
  </div>
</section>

<section class="contact">
  <div class="citem" style="left:163px">
    <svg width="18" height="18" viewBox="0 0 18 18" fill="none" stroke="#c9a632" stroke-width="1.5"><path d="M4 2l3 4-2 2a9 9 0 0 0 5 5l2-2 4 3-2 3C8 17 1 10 2 4z"/></svg>
    <span><b>Contact Us Free</b>&nbsp; (555) 014-2290</span>
  </div>
  <div class="divider" style="left:436px"></div>
  <div class="citem" style="left:476px">
    <svg width="16" height="20" viewBox="0 0 16 20" fill="none" stroke="#c9a632" stroke-width="1.5"><path d="M8 19s6-6.5 6-11A6 6 0 0 0 2 8c0 4.5 6 11 6 11z"/><circle cx="8" cy="8" r="2"/></svg>
    <span><b>Office Address</b>&nbsp; 48 Harbor Lane New York</span>
  </div>
  <div class="divider" style="left:765px"></div>
  <div class="citem" style="left:789px">
    <svg width="18" height="14" viewBox="0 0 18 14" fill="none" stroke="#c9a632" stroke-width="1.5"><rect x="1" y="1" width="16" height="12"/><path d="M1 1l8 7 8-7"/></svg>
    <span><b>Email</b>&nbsp; hello@ardenmoorsecurity.com</span>
  </div>
</section>

<footer class="footer">
  <div class="brand" style="left:150px;top:56px"><span class="mark"></span>ARDENMOOR</div>
  <h4 style="left:449px">QUICK LINKS</h4>
  <div class="flinks" style="left:449px">Burglar Alarms<br>Home Security<br>Business Security</div>
  <div class="flinks" style="left:625px;top:71px">Wireless alarms<br>Monitered Alarms<br>Company background</div>
  <h4 style="left:810px">SOCIAL LINKS</h4>
  <div class="social"><i></i><i></i><i></i><i></i></div>
</footer>
<div class="abs copyright" style="left:0;width:1200px">Copyright © 2021. All rights reserved by. <b>ARDENMOOR</b></div>

</div>
</body>
</html>
```